Bright Harbor Property Institute

This must be done in word press and I will need about 7 tabs The home page, Information page, Schedule and Cost page which will link to a Email me form, a online registration a about us and location/contact tab Each tab will then open several other pages. The home page will describe different courses that we offer since all the schools are about the same you can get a good ideal by going to plomvex.example or keelwardhomeclasses.example and looking at their site I would like mine to be similar as the courses are exactly the same but I would like the site to be more modern I also need it to be in word press so I can change it and update the dates as they change I have attached he logo below

Target Market(s)

people interested in getting into real estate and those who need continuing education

Coding

Number of Pages Required

Font styles to use
Sans Serif

Colors
3276b5

Requirements
Must have
• A page to schedule classes, a tab so the college I am partnering with can link the online courses to the back side, a page that describes the type of classes I offer

```html
<!DOCTYPE html>
<html lang="en">
<head>
<meta charset="utf-8">
<title>Bright Harbor Property Institute</title>
<link href="https://fonts.googleapis.com/css2?family=Arvo:wght@400;700&family=Poppins:wght@300;400;500;600&display=swap" rel="stylesheet">
<style>
:root{
  --blue:#3276b5;
  --blue-dark:#1f5f9f;
  --ink:#1c1c1c;
  --text:#6d6d6d;
  --line:#d9d9d9;
  --black:#000;
  --white:#fff;
  --star:#f6b818;
}
*{margin:0;padding:0;box-sizing:border-box}
html,body{width:1200px;height:3625px;overflow:hidden}
body{position:relative;font-family:'Poppins',sans-serif;color:var(--ink);background:var(--white)}
.abs{position:absolute}
a{color:var(--blue);text-decoration:none}

.top-line{left:0;top:0;width:1200px;height:5px;background:var(--blue)}
.contact-strip{left:560px;top:0;width:546px;height:38px;background:var(--blue);color:#fff;font-size:11px;display:flex;align-items:center;justify-content:center;gap:14px;white-space:nowrap;clip-path:polygon(0 0,100% 0,98% 100%,2% 100%)}
.contact-strip span{display:flex;align-items:center;gap:6px;white-space:nowrap}
.brand{left:94px;top:28px;display:flex;align-items:center;gap:10px}
.brand-dot{width:30px;height:30px;background:var(--blue);border-radius:50%;flex:none}
.brand-name{font-family:'Poppins',sans-serif;font-weight:600;font-size:17px;color:var(--blue);line-height:1.1;width:200px}
.main-nav{right:94px;top:59px;display:flex;gap:30px;font-size:11.5px;font-weight:500;color:var(--ink);white-space:nowrap}

.hero{left:0;top:97px;width:1200px;height:700px;background:linear-gradient(180deg,#0b3a8f 0%,#1c5fc4 30%,#2a66a8 55%,#12233f 70%,#1a3d6a 100%)}
.hero-wave{left:0;top:590px;width:1200px;height:220px}

.eyebrow{font-family:'Arvo',serif;font-size:17px;color:var(--blue);text-align:center;width:1200px;left:0}
.section-title{font-family:'Arvo',serif;font-weight:700;font-size:33px;text-align:center;width:1200px;left:0;letter-spacing:.5px}
.lead{left:145px;width:910px;text-align:center;font-size:12.5px;line-height:20px;color:#444}
.btn{left:516px;top:917px;width:169px;height:30px;background:var(--blue);color:#fff;font-size:12.5px;font-weight:500;display:flex;align-items:center;justify-content:center}

.info-card{top:1090px;width:285px;height:214px;border:1px solid var(--line);border-radius:4px;text-align:center;padding:36px 26px 0}
.info-card h3{font-size:14px;font-weight:600;letter-spacing:.3px;margin-bottom:12px}
.card-text{font-size:11.5px;line-height:19.5px;color:var(--text)}
.dash{font-size:11px;color:var(--text);line-height:14px}
.more{font-size:11.5px;color:var(--blue)}

.services{left:0;top:1369px;width:1200px;height:805px;background:radial-gradient(ellipse at 30% 40%,#4a3a2a 0%,#2a2119 40%,#151210 100%)}
.services-title{color:#fff}
.svc-card{width:315px;height:290px;background:#fff;text-align:center;padding:34px 40px 0}
.svc-icon{width:64px;height:64px;margin:0 auto 10px;display:block}
.svc-card h3{font-size:14.5px;font-weight:600;margin-bottom:10px}

.news-card{top:2307px;width:315px;height:346px;border:1px solid var(--line);border-radius:4px;overflow:hidden}
.news-img{width:100%;height:152px}
.news-date{position:absolute;left:26px;top:128px;width:49px;height:57px;background:var(--blue);color:#fff;text-align:center;font-weight:600;font-size:20px;line-height:24px;padding-top:6px}
.news-date small{display:block;font-size:11px;font-weight:500;line-height:14px}
.news-body{padding:44px 26px 0}
.news-body h3{font-size:14.5px;font-weight:600;margin-bottom:10px}

.avatar{left:562px;top:2803px;width:76px;height:76px;border-radius:50%;background:radial-gradient(circle,#d9a38a,#8a4b3a)}
.stars{left:0;width:1200px;top:2900px;text-align:center;color:var(--star);font-size:19px;letter-spacing:2px}
.quote{left:270px;width:660px;top:2932px;text-align:center;font-size:12.5px;line-height:20px;color:#444}
.reviewer{left:0;width:1200px;top:2978px;text-align:center;font-size:12.5px;color:var(--blue)}
.dots{left:583px;top:3017px;display:flex;gap:6px;z-index:2}
.dots i{display:block;width:7px;height:2px;background:#888}
.dots i.on{background:#222;width:7px}

.footer-wave{left:0;top:2990px;width:1200px;height:160px}
.footer{left:0;top:3140px;width:1200px;height:485px;background:var(--black);color:#bbb}
.foot-brand{left:94px;top:3200px;display:flex;align-items:center;gap:10px}
.foot-brand .brand-name{color:#fff;font-size:19px;width:230px}
.foot-about{left:94px;top:3285px;width:380px;font-size:11.5px;line-height:20px;color:#bbb}
.socials{left:94px;top:3357px;display:flex;gap:6px}
.socials i{display:block;width:25px;height:25px;border-radius:50%;background:#fff}
.foot-head{font-family:'Arvo',serif;font-weight:700;font-size:17px;color:#fff}
.links{font-size:11.5px;line-height:28px;color:#bbb;list-style:none;white-space:nowrap}
.links li::before{content:"»";margin-right:10px;color:#bbb}
.contact-list{font-size:11.5px;color:#bbb;list-style:none}
.contact-list li{display:flex;gap:10px;line-height:17px;margin-bottom:11px}
.join{left:94px;top:3447px;font-family:'Arvo',serif;font-weight:700;font-size:24px;color:#fff}
.subscribe{left:397px;top:3434px;width:658px;height:56px;background:#fff;border-radius:28px}
.subscribe span{position:absolute;left:50px;top:19px;font-size:12.5px;color:#888}
.subscribe b{position:absolute;right:0;top:0;width:209px;height:56px;border-radius:28px;background:var(--blue);color:#fff;font-size:16px;font-weight:600;display:flex;align-items:center;justify-content:center}
.foot-rule{left:94px;top:3531px;width:1012px;height:1px;background:#333}
.copyright{left:0;width:1200px;top:3566px;text-align:center;color:#ddd;font-size:12px}
</style>
</head>
<body>

<div class="abs top-line"></div>
<div class="abs contact-strip">
  <span><svg width="12" height="12" viewBox="0 0 24 24"><path fill="#fff" d="M6.6 10.8a15 15 0 006.6 6.6l2.2-2.2a1 1 0 011-.25 11 11 0 003.5.56 1 1 0 011 1V20a1 1 0 01-1 1A17 17 0 013 4a1 1 0 011-1h3.5a1 1 0 011 1 11 11 0 00.56 3.5 1 1 0 01-.25 1z"/></svg>555 014 2736</span>
  <span><svg width="14" height="11" viewBox="0 0 24 18"><path fill="#fff" d="M0 0h24v18H0zM2 2l10 8 10-8v-.1H2z"/></svg>info@brightharbor.example</span>
  <span><svg width="11" height="14" viewBox="0 0 24 32"><path fill="#fff" d="M12 0a12 12 0 0112 12c0 9-12 20-12 20S0 21 0 12A12 12 0 0112 0zm0 7a5 5 0 100 10 5 5 0 000-10z"/></svg>Tallow Rd #305, Fernmoor, WA, 98017</span>
</div>

<header>
  <div class="abs brand"><span class="brand-dot"></span><span class="brand-name">Bright Harbor Property Institute</span></div>
  <nav class="abs main-nav">
    <span>HOME</span><span>INFORMATION</span><span>SCHEDULE AND COST</span><span>ONLINE REGISTRATION</span><span>ABOUT US</span><span>LOCATION</span><span>CONTACT</span>
  </nav>
</header>

<div class="abs hero" role="img" aria-label="City skyline of glass towers at dusk reflected on the water"></div>
<svg class="abs hero-wave" viewBox="0 0 1200 220" preserveAspectRatio="none">
  <path fill="#3276b5" d="M0 190 C 260 20 640 0 1200 170 L1200 220 L0 220Z"/>
  <path fill="#fff" d="M0 205 C 260 60 640 40 1200 205 L1200 220 L0 220Z"/>
</svg>

<main>
  <section class="intro">
    <p class="abs eyebrow" style="top:780px">Nunc pulvinar tortor a leo</p>
    <h1 class="abs section-title" style="top:805px">SCHEDULE AND COST</h1>
    <p class="abs lead" style="top:858px">Praesent scelerisque venenatis odio, non varius purus pulvinar nec. Maecenas egestas accumsan urna eu laoreet. Nunc scelerisque facilisis diam, sed aliquam libero facilisis ac. Proin quis nisi neque. Etiam non sodales elit. Nunc pulvinar tortor a leo imperdiet, at tincidunt ante volutpat.</p>
    <a class="abs btn">Get Started Todat</a>
  </section>

  <section class="general">
    <p class="abs eyebrow" style="top:1007px">Bright Harbor Property Institute</p>
    <h2 class="abs section-title" style="top:1032px">GENERAL INFORMATION</h2>
    <div class="abs info-card" style="left:146px"><h3>60-HOUR PRE-LICENSING</h3><p class="card-text">Praesent scelerisque venenatis odio, non varius purus pulvinar nec. Maecenas egestas accumsan urna eu laoreet. Nunc scelerisque facilisis diam.</p><p class="dash">-</p><a class="more">Read More</a></div>
    <div class="abs info-card" style="left:459px"><h3>60-HOUR PRE-LICENSING</h3><p class="card-text">Praesent scelerisque venenatis odio, non varius purus pulvinar nec. Maecenas egestas accumsan urna eu laoreet. Nunc scelerisque facilisis diam.</p><p class="dash">-</p><a class="more">Read More</a></div>
    <div class="abs info-card" style="left:770px"><h3>60-HOUR PRE-LICENSING</h3><p class="card-text">Praesent scelerisque venenatis odio, non varius purus pulvinar nec. Maecenas egestas accumsan urna eu laoreet. Nunc scelerisque facilisis diam.</p><p class="dash">-</p><a class="more">Read More</a></div>
  </section>

  <section>
    <div class="abs services" role="img" aria-label="Blurred warm-toned office interior in low light"></div>
    <h2 class="abs section-title services-title" style="top:1428px">THE BRIGHT HARBOR SERVICES</h2>

    <div class="abs svc-card" style="left:94px;top:1491px">
      <svg class="svc-icon" viewBox="0 0 64 64"><rect x="6" y="12" width="30" height="24" rx="2" fill="#fff" stroke="#222" stroke-width="2"/><rect x="10" y="16" width="22" height="16" fill="#5aa0dc"/><rect x="16" y="40" width="40" height="18" rx="3" fill="#f2a33a" stroke="#222" stroke-width="2"/><circle cx="44" cy="26" r="8" fill="#f6c27a" stroke="#222" stroke-width="2"/></svg>
      <h3>Information</h3><p class="card-text">Praesent scelerisque venenatis odio, non varius purus pulvinar nec. Maecenas egestas accumsan urna eu laoreet. Nunc scelerisque facilisis diam.</p><p class="dash">-</p><a class="more">Read More</a>
    </div>
    <div class="abs svc-card" style="left:443px;top:1491px">
      <svg class="svc-icon" viewBox="0 0 64 64"><rect x="6" y="10" width="46" height="46" rx="3" fill="#fff" stroke="#222" stroke-width="2"/><rect x="6" y="10" width="46" height="10" fill="#e2513a" stroke="#222" stroke-width="2"/><g fill="#8fc2ea" stroke="#222"><rect x="12" y="26" width="7" height="6"/><rect x="22" y="26" width="7" height="6"/><rect x="12" y="36" width="7" height="6"/><rect x="22" y="36" width="7" height="6"/><rect x="12" y="46" width="7" height="6"/></g><circle cx="46" cy="46" r="12" fill="#f6c23a" stroke="#222" stroke-width="2"/><path d="M46 39v7h5" stroke="#222" stroke-width="2" fill="none"/></svg>
      <h3>Schedule &amp; Cost</h3><p class="card-text">Praesent scelerisque venenatis odio, non varius purus pulvinar nec. Maecenas egestas accumsan urna eu laoreet. Nunc scelerisque facilisis diam.</p><p class="dash">-</p><a class="more">Read More</a>
    </div>
    <div class="abs svc-card" style="left:791px;top:1491px">
      <svg class="svc-icon" viewBox="0 0 64 64"><rect x="8" y="6" width="48" height="52" fill="#f6d77a" stroke="#222" stroke-width="2"/><rect x="14" y="14" width="14" height="16" fill="#fff" stroke="#222" stroke-width="2"/><g stroke="#222" stroke-width="2"><path d="M34 16h16M34 22h16M34 28h12M14 38h36M14 46h36"/></g></svg>
      <h3>Registration</h3><p class="card-text">Praesent scelerisque venenatis odio, non varius purus pulvinar nec. Maecenas egestas accumsan urna eu laoreet. Nunc scelerisque facilisis diam.</p><p class="dash">-</p><a class="more">Read More</a>
    </div>

    <div class="abs svc-card" style="left:94px;top:1815px">
      <svg class="svc-icon" viewBox="0 0 64 64"><rect x="6" y="14" width="44" height="44" rx="2" fill="#5aa0dc" stroke="#222" stroke-width="2"/><rect x="36" y="4" width="22" height="16" rx="2" fill="#f6d23a" stroke="#222" stroke-width="2"/><path d="M28 30l12 5-12 5-12-5z" fill="#333"/><rect x="18" y="44" width="20" height="14" fill="#fff" stroke="#222" stroke-width="2"/></svg>
      <h3>Online Courses</h3><p class="card-text">Praesent scelerisque venenatis odio, non varius purus pulvinar nec. Maecenas egestas accumsan urna eu laoreet. Nunc scelerisque facilisis diam.</p><p class="dash">-</p><a class="more">Read More</a>
    </div>
    <div class="abs svc-card" style="left:443px;top:1815px">
      <svg class="svc-icon" viewBox="0 0 64 64"><circle cx="32" cy="32" r="26" fill="#fff" stroke="#222" stroke-width="2"/><path d="M14 52a18 14 0 0136 0" fill="#5aa0dc" stroke="#222" stroke-width="2"/><circle cx="32" cy="28" r="9" fill="#f6c23a" stroke="#222" stroke-width="2"/></svg>
      <h3>Why Bright Harbor?</h3><p class="card-text">Praesent scelerisque venenatis odio, non varius purus pulvinar nec. Maecenas egestas accumsan urna eu laoreet. Nunc scelerisque facilisis diam.</p><p class="dash">-</p><a class="more">Read More</a>
    </div>
    <div class="abs svc-card" style="left:791px;top:1815px">
      <svg class="svc-icon" viewBox="0 0 64 64"><circle cx="18" cy="18" r="12" fill="#5aa0dc" stroke="#222" stroke-width="2"/><rect x="34" y="6" width="26" height="16" rx="3" fill="#fff" stroke="#222" stroke-width="2"/><text x="47" y="18" font-size="10" text-anchor="middle" font-family="Poppins,sans-serif" font-weight="600">24h</text><path d="M14 60a18 16 0 0136 0" fill="#f6c23a" stroke="#222" stroke-width="2"/><circle cx="32" cy="36" r="9" fill="#f6d7a8" stroke="#222" stroke-width="2"/></svg>
      <h3>Get in Touch</h3><p class="card-text">Praesent scelerisque venenatis odio, non varius purus pulvinar nec. Maecenas egestas accumsan urna eu laoreet. Nunc scelerisque facilisis diam.</p><p class="dash">-</p><a class="more">Contact Us</a>
    </div>
  </section>

  <section class="news">
    <p class="abs eyebrow" style="top:2233px">learn more from news</p>
    <h2 class="abs section-title" style="top:2258px">RECENT NEWS</h2>
    <article class="abs news-card" style="left:94px">
      <div class="news-img" role="img" aria-label="Person studying at a desk with an open book" style="background:linear-gradient(135deg,#6b4a32,#c9a27a 60%,#e6d2b8)"></div>
      <div class="news-date">23<small>june</small></div>
      <div class="news-body"><h3>Nunc pulvinar tortor a imperdiet</h3><p class="card-text">Praesent scelerisque venenatis odio, non varius purus pulvinar nec. Maecenas egestas accumsan urna eu laoreet.</p><p class="dash">-</p><a class="more">Read More</a></div>
    </article>
    <article class="abs news-card" style="left:443px">
      <div class="news-img" role="img" aria-label="Students working at computers in a classroom" style="background:linear-gradient(135deg,#3a2c26,#9a8a7a 55%,#d8cfc4)"></div>
      <div class="news-date">23<small>june</small></div>
      <div class="news-body"><h3>Nunc pulvinar tortor a imperdiet</h3><p class="card-text">Praesent scelerisque venenatis odio, non varius purus pulvinar nec. Maecenas egestas accumsan urna eu laoreet.</p><p class="dash">-</p><a class="more">Read More</a></div>
    </article>
    <article class="abs news-card" style="left:792px">
      <div class="news-img" role="img" aria-label="Alarm clock on a stack of books beside a cup of pencils" style="background:linear-gradient(135deg,#f2f2f2,#cfcfcf 60%,#8a7a6a)"></div>
      <div class="news-date">23<small>june</small></div>
      <div class="news-body"><h3>Nunc pulvinar tortor a imperdiet</h3><p class="card-text">Praesent scelerisque venenatis odio, non varius purus pulvinar nec. Maecenas egestas accumsan urna eu laoreet.</p><p class="dash">-</p><a class="more">Read More</a></div>
    </article>
  </section>

  <section class="testimonial">
    <p class="abs eyebrow" style="top:2713px">Client's Documentary</p>
    <h2 class="abs section-title" style="top:2738px">TESTIMONIAL</h2>
    <div class="abs avatar" role="img" aria-label="Client portrait"></div>
    <p class="abs stars">★★★★★</p>
    <p class="abs quote">Praesent scelerisque venenatis odio, non varius purus pulvinar nec. Maecenas egestas accumsan urna eu laoreet. Nunc scelerisque facilisis diam, sed aliquam libero facilisis ac. Proin quis nisi neque.</p>
    <p class="abs reviewer">Mara Ellington</p>
  </section>
</main>

<svg class="abs footer-wave" viewBox="0 0 1200 160" preserveAspectRatio="none">
  <path fill="#3276b5" d="M0 20 C 300 80 700 150 1200 70 L1200 160 L0 160Z"/>
  <path fill="#000" d="M0 50 C 300 115 700 165 1200 100 L1200 160 L0 160Z"/>
</svg>
<div class="abs dots"><i></i><i class="on"></i><i></i></div>

<footer>
  <div class="abs footer"></div>
  <div class="abs foot-brand"><span class="brand-dot" style="background:#fff"></span><span class="brand-name">Bright Harbor Property Institute</span></div>
  <p class="abs foot-about">Nunc pulvinar tortor a leo imperdiet, at tincidunt ante volutpat. Cras commodo sodales leo, a convallis dolor suscipit vitae. Cras vel pretium ex. Suspendisse imperdiet.</p>
  <div class="abs socials"><i></i><i></i><i></i><i></i></div>

  <h4 class="abs foot-head" style="left:539px;top:3240px">Quick Link</h4>
  <ul class="abs links" style="left:539px;top:3283px"><li>Home</li><li>Information</li><li>Schedule And Cost</li><li>Online Registration</li></ul>
  <ul class="abs links" style="left:698px;top:3283px"><li>About us</li><li>Location</li><li>Contact</li></ul>

  <h4 class="abs foot-head" style="left:845px;top:3240px">Contact Us</h4>
  <ul class="abs contact-list" style="left:845px;top:3290px;width:200px">
    <li><svg width="11" height="14" viewBox="0 0 24 32"><path fill="#fff" d="M12 0a12 12 0 0112 12c0 9-12 20-12 20S0 21 0 12A12 12 0 0112 0zm0 7a5 5 0 100 10 5 5 0 000-10z"/></svg><span>Tallow Rd #305, Fernmoor,<br>WA, 98017</span></li>
    <li><svg width="12" height="12" viewBox="0 0 24 24"><path fill="#fff" d="M6.6 10.8a15 15 0 006.6 6.6l2.2-2.2a1 1 0 011-.25 11 11 0 003.5.56 1 1 0 011 1V20a1 1 0 01-1 1A17 17 0 013 4a1 1 0 011-1h3.5a1 1 0 011 1 11 11 0 00.56 3.5 1 1 0 01-.25 1z"/></svg><span>555 014 2736</span></li>
    <li><svg width="13" height="10" viewBox="0 0 24 18"><path fill="#fff" d="M0 0h24v18H0zM2 2l10 8 10-8v-.1H2z"/></svg><span>info@brightharbor.example</span></li>
  </ul>

  <p class="abs join">Join for New Updates</p>
  <div class="abs subscribe"><span>Enter Your Email Id</span><b>Subscribe Now</b></div>
  <div class="abs foot-rule"></div>
  <p class="abs copyright">© copyright 2019 by Bright Harbor Property Institute. All Rights Reserved</p>
</footer>

</body>
</html>
```